Top Producing Realtor Business Card Design

Looking for branding with my logo on all of my materials. I am a top producing real estate agent, selling expensive homes in California. I'm looking for a classy design that includes my existing logo, the company corporate logo and my photo.

Looking forward to your submissions! Thank you so much! :)

I appreciate your submissions very much!  Excellent work!  I have revised the brief to be more clear about what I think I'm looking for.  Keep the submissions coming in!!  Thank you so much :)

Target Market(s)

Wealthy home buyers and sellers in California.

Industry/Entity Type

Real Estate

Requirements
Must have
• Must include:

Homestead Pinnacle Logo

Below Homestead Pinnacle Logo it must say: Ashford Vale (Helvetica font)

Complete address: 58317 Barwick Street
Ashford Vale, WV 94687

Phone number: 415.962.3057 cell
415.740.2195 VM 5821 office

My photo

My name: Mara Quinlow (please make sure it's correct before you submit) :)

My MQ Logo (if possible please keep logo colors the same)

"Realtor" with a reserved symbol after or below my name

My license number: StaREB #07428915

My website: www.MaraQuinlow-example.com

My email: Mara@MaraQuinlow-example.com

Nice to have
• I'm open minded :) The main goal is to have the MQ logo is on all of my material. For the business cards I sort of imagine my MQ logo in the background, and I like a fade. I prefer the logo to be on the front of the card, and I like it on the back of the card too, So a two sided business card is ok.

I prefer the light blue Homestead Pinnacle Logo submitted. Please note the light blue color must closely match :)

Another idea is the business card can be in the format of the yard sign photo submitted (maybe changed into the light blue color), to possibly be a business card that looks like the yard sign. The yard sign layout must closely match the example submitted due to corporate guidelines.

Basically I'm looking for something that will tie everything together with my photo and logo so it's well branded in the clients mind. :)

Should not have
• Please keep the logo's exactly as they are, including color...no need to change.

If you choose to use the yard sign example provided for the business card, Please do not change the basic layout of the yard sign submitted, I have to follow the corporate standards.

```html
<!DOCTYPE html>
<html lang="en">
<head>
<meta charset="utf-8">
<title>Mara Quinlow – Realtor Business Card</title>
<link rel="stylesheet" href="https://fonts.googleapis.com/css2?family=Open+Sans:wght@300;600&family=Arimo:wght@400;700&display=swap">
<style>
  :root {
    --slate: #868f93;
    --slate-dark: #7d868a;
    --ink: #111111;
    --white: #ffffff;
    --contact: #f2f4f5;
    --gold-edge: #c4900e;
    --gold-mid: #e9ee22;
    --gold-deep: #d8b313;
    --stripe: #dfe9ec;
    --photo-top: #b7b0a6;
    --photo-bottom: #2b2a2c;
  }
  html, body {
    margin: 0;
    padding: 0;
    overflow: hidden;
    background: var(--slate);
  }
  .card {
    position: relative;
    width: 1200px;
    height: 699px;
    overflow: hidden;
    background: var(--slate);
    font-family: "Open Sans", Arial, sans-serif;
  }
  .card-art {
    position: absolute;
    inset: 0;
  }
  .agent-brand {
    position: absolute;
    left: 87px;
    top: 216px;
    width: 240px;
    text-align: center;
    color: var(--white);
    font-weight: 600;
    white-space: nowrap;
  }
  .agent-name {
    font-size: 27px;
    line-height: 1.1;
  }
  .agent-title {
    font-size: 16px;
    letter-spacing: 1.2px;
    line-height: 1.2;
  }
  .agent-title sup {
    font-size: 8px;
  }
  .contact-list {
    position: absolute;
    left: 97px;
    top: 290px;
    margin: 0;
    padding: 0;
    list-style: none;
    color: var(--contact);
    font-weight: 300;
    font-size: 25.5px;
    line-height: 31.7px;
    white-space: nowrap;
  }
  .website {
    position: absolute;
    left: 100px;
    top: 594px;
    font-family: "Arimo", Helvetica, Arial, sans-serif;
    font-weight: 700;
    font-size: 24px;
    color: var(--ink);
    white-space: nowrap;
  }
  .brokerage {
    position: absolute;
    left: 935px;
    top: 488px;
    width: 175px;
    text-align: center;
    font-family: "Arimo", Helvetica, Arial, sans-serif;
    color: var(--ink);
  }
  .brokerage-name {
    font-size: 24px;
    font-weight: 700;
    line-height: 1.15;
    height: 102px;
    display: flex;
    align-items: center;
    justify-content: center;
  }
  .brokerage-office {
    margin-top: 6px;
    font-size: 23px;
    font-weight: 400;
    white-space: nowrap;
  }
</style>
</head>
<body>
<main class="card">
  <svg class="card-art" width="1200" height="699" viewBox="0 0 1200 699">
    <defs>
      <linearGradient id="photo-fill" x1="0" y1="0" x2="0" y2="1">
        <stop offset="0" stop-color="var(--photo-top)"/>
        <stop offset="0.55" stop-color="#8d7f6e"/>
        <stop offset="1" stop-color="var(--photo-bottom)"/>
      </linearGradient>
      <linearGradient id="gold-band" x1="0" y1="0" x2="1" y2="0">
        <stop offset="0" stop-color="var(--gold-edge)"/>
        <stop offset="0.5" stop-color="var(--gold-mid)"/>
        <stop offset="0.85" stop-color="var(--gold-deep)"/>
        <stop offset="1" stop-color="var(--gold-edge)"/>
      </linearGradient>
      <linearGradient id="stripe-fill" x1="0" y1="0" x2="1" y2="0">
        <stop offset="0" stop-color="#b9c6ca"/>
        <stop offset="0.6" stop-color="var(--stripe)"/>
        <stop offset="1" stop-color="var(--white)"/>
      </linearGradient>
    </defs>
    <rect class="backdrop" x="0" y="0" width="1200" height="699" fill="var(--slate)"/>
    <rect class="agent-photo" x="709" y="74" width="391" height="440" rx="30" fill="url(#photo-fill)" role="img" aria-label="Portrait photo of Mara Quinlow, realtor"/>
    <path class="accent-stripe" d="M0 515 Q700 478 1200 392 L1200 408 Q700 500 0 532 Z" fill="url(#stripe-fill)"/>
    <path class="gold-band" d="M0 532 Q700 500 1200 408 L1200 661 L0 661 Z" fill="url(#gold-band)"/>
    <rect class="base-strip" x="0" y="661" width="1200" height="38" fill="var(--slate-dark)"/>
  </svg>

  <div class="agent-brand">
    <div class="agent-name">Mara Quinlow</div>
    <div class="agent-title">REALTOR<sup>®</sup></div>
  </div>

  <ul class="contact-list">
    <li>StaREB #07428915</li>
    <li>Mara@MaraQuinlow-example.com</li>
    <li>415.962.3057 Cell</li>
    <li>415.740.2195 VM 5821 Office</li>
    <li>58317 Barwick Street,</li>
    <li>Ashford Vale, WV 94687</li>
  </ul>

  <div class="website">www.MaraQuinlow-example.com</div>

  <div class="brokerage">
    <div class="brokerage-name">Homestead Pinnacle</div>
    <div class="brokerage-office">Ashford Vale</div>
  </div>
</main>
</body>
</html>
```